Great Opportunity !! Masters in Business Analytics College Course

the size is Full Page, with bleed*
8”x 10.75" plus 0.25" bleed.
please leave one inch for footer
the purpose is attract students to join this college program .
this is for students in USA .
college age of around 24 years old
I am looking for a flyer that is unique and shows creativity .
A flyer that people would want to look at it because it is unique.
you can choose either vector, text ,or picture.
if you do picture it should be a white USA citizen wearing a white solid shirt and not long hair

Target Market(s)

USA students about 23 in age to join this college program

Industry/Entity Type

education

Colors
0054AA
0677BA
7BADD7
CADEEF
E8F1F8
0094D4
00A9DD
6FCCEA
C7EBF8
E9F6FB

Requirements
Must have
• the text should not be crowded .. .. .. the ad should not be full of text
Should not have
• not have very large text .. it should not be a flyer that is full of text .. you have to figure out how to avoid looking at the ad and it is very busy with text

```html
<!DOCTYPE html>
<html lang="en">
<head>
<meta charset="UTF-8">
<title>Master's in Business Analytics – Flyer</title>
<link href="https://fonts.googleapis.com/css2?family=Prompt:wght@400;500;600;700&display=swap" rel="stylesheet">
<style>
  :root{
    --page-bg:#333333;
    --paper:#ffffff;
    --brand-blue:#0d4fa8;
    --button-blue:#1055a6;
    --band-teal:#2a8fc8;
    --band-blue:#2f66b4;
    --band-purple:#4e3f8a;
    --stripe:#eeeeee;
    --ink:#141414;
    --ice:#7badd7;
    --mist:#e8f1f8;
  }
  *{box-sizing:border-box;margin:0;padding:0}
  html,body{width:997px;height:1200px;overflow:hidden;background:var(--page-bg)}
  body{font-family:"Prompt",sans-serif;position:relative}
  .flyer{position:absolute;left:52px;top:0;width:893px;height:1200px;background:var(--paper);overflow:hidden}
  .header{position:absolute;left:0;top:0;width:100%;height:135px;
    background:repeating-linear-gradient(to bottom,var(--paper) 0 8px,var(--stripe) 8px 16px,var(--paper) 16px 26px)}
  .header-title{position:absolute;left:0;top:36px;width:100%;text-align:center;color:var(--brand-blue);
    font-weight:700;font-size:31px;line-height:33px}
  .hero{position:absolute;left:0;top:135px;width:100%;height:515px;
    background:linear-gradient(115deg,var(--band-teal) 0%,var(--band-blue) 40%,var(--band-blue) 55%,var(--band-purple) 100%)}
  .hero-art{position:absolute;left:92px;top:49px;width:291px;height:364px;border-radius:8px;
    background:radial-gradient(circle at 45% 45%,#6e6fd0 0%,#4a52b8 45%,rgba(60,90,180,0) 75%)}
  .hero-copy{position:absolute;left:432px;top:96px;color:var(--paper)}
  .hero-title{font-weight:700;font-size:25px;line-height:33px}
  .hero-body{margin-top:23px;font-size:23px;line-height:30px}
  .salary{background:#000;padding:0 8px;font-weight:600}
  .hero-source{margin-top:42px;font-size:18px}
  .roles{position:absolute;top:580px;left:0;width:100%}
  .role{position:absolute;top:0;width:173px;height:130px;background:var(--paper);text-align:center}
  .role svg{margin-top:26px}
  .role-label{position:absolute;left:0;width:100%;top:104px;color:var(--brand-blue);font-size:16px}
  .role-bi{left:133px}.role-analyst{left:360px}.role-scientist{left:586px}
  .network-fade{position:absolute;left:0;top:720px;width:100%;height:367px;
    background:linear-gradient(160deg,rgba(255,255,255,0) 45%,var(--mist) 65%,var(--ice) 100%)}
  .tag{position:absolute;top:774px;width:266px;height:45px;background:var(--button-blue);color:var(--paper);
    font-size:18px;text-align:center;line-height:45px}
  .tag-hired{left:124px}.tag-open{left:544px}
  .employers{position:absolute;top:862px;left:63px;display:flex;gap:30px;align-items:center;
    font-weight:600;font-size:19px;color:var(--ink)}
  .employer{display:flex;align-items:center;gap:6px}
  .employer-dot{width:14px;height:14px;border-radius:50%;background:var(--ink)}
  .event{position:absolute;left:554px;top:838px;color:var(--brand-blue);font-size:20px}
  .event-row{display:flex;align-items:center;gap:14px;height:33px}
  .notes{position:absolute;left:63px;top:964px;color:var(--ink);font-size:14.5px;line-height:19px}
  .notes .format{margin-top:27px}
</style>
</head>
<body>
<main class="flyer">
  <header class="header">
    <h1 class="header-title">Do you have an analytical mind?<br>Are you seeking a profitable career?</h1>
  </header>

  <section class="hero">
    <div class="hero-art" role="img" aria-label="Isometric illustration of analysts at desks beside a large dashboard screen with a magnifying glass"></div>
    <div class="hero-copy">
      <h2 class="hero-title">A Master's in Business Analytics<br>Ridgefield State University **</h2>
      <p class="hero-body">can prepare you for<br>in-demand jobs with a<br>median salary of <span class="salary">$100k+</span></p>
      <p class="hero-source">The National Labor Data Survey 2023</p>
    </div>
  </section>

  <div class="network-fade" role="img" aria-label="Soft light-blue network of connected lines and dots"></div>

  <section class="roles">
    <div class="role role-bi">
      <svg width="60" height="60" viewBox="0 0 60 60" fill="none" stroke="#0d4fa8" stroke-width="2">
        <path d="M28 8c-6 0-9 4-9 7-5 0-8 4-7 9-4 2-4 9 0 11-1 5 3 9 8 9 1 4 4 6 8 6z"/>
        <path d="M28 14h10l4-4M28 24h16M28 34h12l4 4M28 44h8"/>
        <circle cx="45" cy="9" r="2.5"/><circle cx="47" cy="24" r="2.5"/><circle cx="47" cy="40" r="2.5"/><circle cx="39" cy="44" r="2.5"/>
      </svg>
      <span class="role-label">BI Developer</span>
    </div>
    <div class="role role-analyst">
      <svg width="60" height="60" viewBox="0 0 60 60" fill="none" stroke="#0d4fa8" stroke-width="2">
        <path d="M4 56h52"/>
        <rect x="8" y="40" width="7" height="16"/><rect x="20" y="34" width="7" height="22"/>
        <rect x="32" y="42" width="7" height="14"/><rect x="44" y="30" width="7" height="26"/>
        <path d="M10 28l12-10 10 6 12-12"/>
        <circle cx="10" cy="28" r="2.5"/><circle cx="22" cy="18" r="2.5"/><circle cx="32" cy="24" r="2.5"/>
        <circle cx="50" cy="8" r="6"/><path d="M50 5v6"/>
      </svg>
      <span class="role-label">Data Analyst</span>
    </div>
    <div class="role role-scientist">
      <svg width="60" height="60" viewBox="0 0 60 60" fill="none" stroke="#0d4fa8" stroke-width="2">
        <path d="M22 6h14M25 6v18L12 50c-1 3 1 6 4 6h26c3 0 5-3 4-6L33 24V6"/>
        <path d="M17 40h24"/>
        <circle cx="26" cy="47" r="2"/><circle cx="34" cy="50" r="1.5"/>
        <circle cx="48" cy="14" r="3"/><circle cx="52" cy="26" r="2"/>
      </svg>
      <span class="role-label">Data Scientist</span>
    </div>
  </section>

  <div class="tag tag-hired">Graduates were hired at:</div>
  <div class="tag tag-open">Open House</div>

  <div class="employers">
    <span class="employer"><span class="employer-dot"></span>Halvern</span>
    <span class="employer">Brightwell</span>
    <span class="employer">Norcom</span>
    <span class="employer">Voltera</span>
  </div>

  <div class="event">
    <div class="event-row">
      <svg width="22" height="20" viewBox="0 0 22 20"><rect x="1" y="3" width="20" height="16" rx="2" fill="#1d9bd8"/><rect x="1" y="3" width="20" height="4" fill="#1270b8"/><g fill="#fff"><rect x="4" y="9" width="3" height="3"/><rect x="9.5" y="9" width="3" height="3"/><rect x="15" y="9" width="3" height="3"/><rect x="4" y="14" width="3" height="3"/><rect x="9.5" y="14" width="3" height="3"/></g></svg>
      <span>Wed., April 20, 7:30 pm</span>
    </div>
    <div class="event-row">
      <svg width="22" height="16" viewBox="0 0 22 16"><rect x="0" y="0" width="22" height="16" rx="2" fill="#1d9bd8"/><path d="M1 1l10 8 10-8" fill="none" stroke="#fff" stroke-width="1.6"/></svg>
      <span>alexreed@mailbox.com</span>
    </div>
  </div>

  <footer class="notes">
    <p>*** GBEA Accreditation.</p>
    <p>This distinction is held by only 5% of business schools globally.</p>
    <p class="format">Hybrid / one weekly session</p>
  </footer>
</main>
</body>
</html>
```